BRAVEN POWERLINE SERVICES needs a vibrant design for electrical contracting work.

I require a card design for my own electrical contracting business. I will be doing a lot of domestic and commercial work, including things such as repairs, maintenance, lighting, installations and various others. LED lighting and energy efficiency will be a big part of my business. I wish not to have childish pictures such as light bulbs in the design, but rather a smart and modern looking card which incorporates my logo colours and perhaps the same lighting strike within the faded background of the card.

Target Market(s)

Residential and Commercial property owners.

Industry/Entity Type

Electrical

Contact Information for Business Card

Dalen Voskic
EC40923
Phone Number: 0417 358 942
Email: dalen@bravenpowerline.com

Font styles to use
Serif
Sans Serif

Requirements
Must have
• My Logo and associated colours.
Nice to have
• Some form of shapes splitting the card into different colours related to the colours of my logo. Electric Blue, Silver/Grey and White.
Should not have
• Childish pictures and symbols such as light bulbs.

```html
<!DOCTYPE html>
<html lang="en">
<head>
<meta charset="utf-8">
<title>Braven Powerline Services – Business Card</title>
<link href="https://fonts.googleapis.com/css2?family=Marcellus+SC&family=Source+Sans+3:wght@400;700&display=swap" rel="stylesheet">
<style>
  :root {
    --blue-deep: #07078c;
    --blue-mid: #4747e0;
    --blue-brand: #1414d8;
    --silver-light: #f2f2f4;
    --silver-mid: #c9c9cf;
    --silver-dark: #8d8d95;
    --white: #ffffff;
  }
  html, body {
    margin: 0;
    padding: 0;
    width: 1200px;
    height: 750px;
    overflow: hidden;
    background: var(--white);
  }
  .card {
    position: relative;
    width: 1200px;
    height: 750px;
    overflow: hidden;
    background: linear-gradient(180deg,
      var(--blue-deep) 0%,
      #1a1ab0 30%,
      var(--blue-mid) 50%,
      #1a1ab0 72%,
      var(--blue-deep) 100%);
    font-family: "Source Sans 3", Arial, sans-serif;
    color: var(--white);
  }
  .emblem-area {
    position: absolute;
    left: 0;
    top: 0;
    width: 1200px;
    height: 750px;
  }
  .brand-plate {
    position: absolute;
    left: 55px;
    top: 60px;
    width: 552px;
    height: 166px;
    background: var(--white);
    box-shadow: 3px 4px 6px rgba(0, 0, 0, 0.45);
    display: flex;
    align-items: center;
    gap: 22px;
    padding: 0 24px;
    box-sizing: border-box;
  }
  .brand-dot {
    flex: none;
    width: 96px;
    height: 96px;
    border-radius: 50%;
    background: var(--blue-brand);
  }
  .brand-name {
    margin: 0;
    font-family: "Source Sans 3", Arial, sans-serif;
    font-weight: 700;
    color: var(--blue-brand);
    line-height: 1;
    letter-spacing: 1px;
  }
  .brand-name .line-main { display: block; font-size: 64px; }
  .brand-name .line-sub { display: block; font-size: 30px; margin-top: 8px; }
  .rule {
    position: absolute;
    left: 52px;
    width: 541px;
    height: 5px;
    background: var(--white);
  }
  .rule--top { top: 294px; }
  .rule--bottom { top: 455px; }
  .holder-name {
    position: absolute;
    left: 52px;
    top: 332px;
    margin: 0;
    font-family: "Marcellus SC", Georgia, serif;
    font-weight: 400;
    font-size: 72px;
    line-height: 1;
    letter-spacing: 1px;
  }
  .contact-list {
    position: absolute;
    left: 55px;
    top: 497px;
    margin: 0;
    padding: 0;
    list-style: none;
    font-size: 39px;
    line-height: 71px;
  }
</style>
</head>
<body>
  <div class="card">
    <svg class="emblem-area" viewBox="0 0 1200 750" role="img" aria-label="Large faded brand emblem in silver with electric-blue accent">
      <defs>
        <radialGradient id="silver-disc" cx="0.55" cy="0.45" r="0.6">
          <stop offset="0" stop-color="var(--silver-light)"/>
          <stop offset="0.6" stop-color="var(--silver-mid)"/>
          <stop offset="1" stop-color="var(--silver-dark)"/>
        </radialGradient>
      </defs>
      <circle cx="1010" cy="372" r="372" fill="url(#silver-disc)"/>
    </svg>

    <div class="brand-plate">
      <span class="brand-dot"></span>
      <h1 class="brand-name">
        <span class="line-main">BRAVEN</span>
        <span class="line-sub">POWERLINE SERVICES</span>
      </h1>
    </div>

    <div class="rule rule--top"></div>
    <h2 class="holder-name">Dalen Voskic</h2>
    <div class="rule rule--bottom"></div>

    <ul class="contact-list">
      <li>EC40923</li>
      <li>P: 0417 358 942</li>
      <li>E: dalen@bravenpowerline.com</li>
    </ul>
  </div>
</body>
</html>
```